Letterhead design - Harwick Group

We have just had our Logo created and our now wantng a letterhead design to incorporate this. Please use the same colours as in the logo, which is attached.
Please use the company details below
P O Box 86, Bleneheim 7315
Ph: 03 642 1937
dave@harwickgroup.co.nz
We would like a professional look
We need an overall letterhead design for our varied group of buisinesses which are based in NZ and overseas. We grow and develop buisinesses. Our companies began in NZ but we now have branches overseas as well. People are our greatest asset and we employ some incredible staff. Our buisinesses are scientific, innovative and growing in size and expertise with a financial base.

Target Market(s)

Professionals

Industry/Entity Type

Investment

Requirements
Must have
• Easy to read.
• Please use the same colours as in the logo
• Please use the company details below
• P O Box 86, Bleneheim 7315
• Ph: 03 642 1937
• dave@harwickgroup.co.nz

```html
<!DOCTYPE html>
<html lang="en">
<head>
<meta charset="utf-8">
<title>Harwick Group Letterhead</title>
<link rel="stylesheet" href="https://fonts.googleapis.com/css2?family=Lato:wght@700;900&display=swap">
<style>
  :root {
    --slate: #556366;
    --lime: #44f544;
    --paper: #ffffff;
    --backdrop: #f2f3f3;
  }
  * { margin: 0; padding: 0; box-sizing: border-box; }
  html, body {
    width: 1200px; height: 1200px; overflow: hidden;
    background: var(--backdrop);
  }
  .letterhead {
    position: absolute; left: 210px; top: 77px;
    width: 735px; height: 1050px;
    background: var(--paper);
    font-family: "Lato", sans-serif;
  }
  .header-band, .footer-band {
    position: absolute; left: 0; width: 735px; display: block;
  }
  .header-band { top: 0; height: 42px; }
  .footer-band { bottom: 0; height: 40px; }
  .company-name {
    position: absolute; left: 26px; top: 62px;
    display: flex; align-items: center; gap: 12px;
    font-size: 34px; font-weight: 900; letter-spacing: 0.5px;
    color: var(--lime); text-transform: uppercase;
  }
  .company-name .mark-square {
    width: 40px; height: 40px; background: var(--lime);
  }
  .contact-block {
    position: absolute; left: 429px; top: 51px;
    height: 67px; border-left: 1.5px solid var(--slate);
    padding-left: 12px;
    display: flex; flex-direction: column; justify-content: space-between;
  }
  .contact-item {
    display: flex; align-items: center; gap: 12px;
    font-size: 14.5px; font-weight: 700; color: var(--slate);
    line-height: 18px; text-transform: uppercase;
  }
  .contact-item svg { width: 14px; height: 14px; flex: none; }
</style>
</head>
<body>
  <main class="letterhead">
    <svg class="header-band" viewBox="0 0 735 42" aria-hidden="true">
      <rect width="735" height="42" fill="var(--slate)"/>
      <polygon points="149,0 586,0 571,31 166,31" fill="var(--lime)"/>
    </svg>

    <div class="company-name"><span class="mark-square"></span>Harwick Group</div>

    <address class="contact-block">
      <div class="contact-item">
        <svg viewBox="0 0 24 24"><path fill="var(--slate)" d="M6.6 10.8a15.1 15.1 0 0 0 6.6 6.6l2.2-2.2c.3-.3.7-.4 1-.2 1.1.4 2.3.6 3.6.6.6 0 1 .4 1 1V20c0 .6-.4 1-1 1A17 17 0 0 1 3 4c0-.6.4-1 1-1h3.5c.6 0 1 .4 1 1 0 1.3.2 2.5.6 3.6.1.3 0 .7-.2 1z"/></svg>
        03 642 1937
      </div>
      <div class="contact-item">
        <svg viewBox="0 0 24 24" fill="none" stroke="var(--slate)" stroke-width="1.5"><circle cx="12" cy="12" r="10"/><ellipse cx="12" cy="12" rx="4.5" ry="10"/><path d="M2 12h20M4 7h16M4 17h16"/></svg>
        P O Box 86, Bleneheim 7315
      </div>
      <div class="contact-item">
        <svg viewBox="0 0 24 24" fill="none" stroke="var(--slate)" stroke-width="1.6"><path d="M12 22s7-7.5 7-13a7 7 0 0 0-14 0c0 5.5 7 13 7 13z"/><circle cx="12" cy="9" r="2.5"/></svg>
        dave@harwickgroup.co.nz
      </div>
    </address>

    <svg class="footer-band" viewBox="0 0 735 40" aria-hidden="true">
      <rect width="735" height="8" fill="var(--slate)"/>
      <rect y="8" width="735" height="32" fill="var(--lime)"/>
      <polygon points="380,8 397,8 364,40 347,40" fill="var(--slate)"/>
    </svg>
  </main>
</body>
</html>
```